Sales Brochure- Generic Line Card 215mm x 140mm

Design a double-sided brochure similar to the attached sample. Cover Page contains a logo and theme that never changes. However, the background picture and the description text on the lower corner will be changed to advertise multiple services. Reverse-side contains Detailed Descriptive text related to the picture on Cover Page as well as Logo and Contact information for the business. Use the Ridgeline Controls website www.ridgelinecontrols.ca for theme, color and contact information. Also, use attached business card design for theme to match. Use the supplied logo. SIZE 215mm x 140mm

Font styles to use
Sans Serif

Colors

Designer to choose colors to be used in the design.

Requirements
Must have
• Look Similar to Sample Brochure but include Ridgeline Controls theme and colors

```html
<!DOCTYPE html>
<html lang="en">
<head>
<meta charset="utf-8">
<title>Ridgeline Controls – Precision CNC Machining Line Card</title>
<link rel="stylesheet" href="https://fonts.googleapis.com/css2?family=Mulish:wght@400;500;600;800&display=swap">
<style>
  :root {
    --teal-deep: #0b555b;
    --teal: #1a8a90;
    --teal-light: #4cc3c6;
    --teal-shadow: #073f44;
    --orange: #f15a1f;
    --orange-text: #e8541a;
    --ink: #1d1d1d;
    --metal-light: #f1f2f3;
    --metal-mid: #c9cccf;
    --metal-dark: #9da1a5;
    --page: #f4f4f4;
    --white: #ffffff;
  }
  * { box-sizing: border-box; margin: 0; padding: 0; }
  html, body { width: 1200px; height: 1000px; overflow: hidden; }
  body {
    position: relative;
    background: var(--page);
    font-family: "Mulish", "Helvetica Neue", Arial, sans-serif;
    color: var(--ink);
  }
  .card {
    position: absolute;
    left: 251px;
    width: 734px;
    height: 478px;
    overflow: hidden;
    background: var(--white);
    box-shadow: 0 3px 8px rgba(0,0,0,.35);
  }
  .card--front { top: 10px; }
  .card--back { top: 510px; }

  /* Front */
  .cover-photo {
    position: absolute; inset: 0;
    background:
      radial-gradient(ellipse 30% 22% at 92% 58%, rgba(110,230,235,.55), transparent 70%),
      radial-gradient(ellipse 45% 30% at 52% 48%, rgba(60,170,175,.55), transparent 70%),
      radial-gradient(ellipse 40% 25% at 78% 22%, rgba(90,195,200,.45), transparent 70%),
      radial-gradient(ellipse 35% 40% at 15% 62%, rgba(7,63,68,.7), transparent 70%),
      radial-gradient(ellipse 50% 30% at 60% 75%, rgba(7,63,68,.55), transparent 70%),
      radial-gradient(ellipse 40% 25% at 30% 18%, rgba(40,140,145,.5), transparent 70%),
      linear-gradient(160deg, var(--teal-deep) 0%, var(--teal) 45%, #126a70 75%, var(--teal-shadow) 100%);
  }
  .brand {
    position: absolute;
    display: flex; align-items: center; gap: 9px;
    font-weight: 800; text-transform: uppercase; letter-spacing: .5px;
    white-space: nowrap;
  }
  .brand__mark { width: 15px; height: 15px; flex: none; }
  .brand--cover { left: 34px; top: 36px; font-size: 25px; color: var(--white); }
  .brand--cover .brand__mark { background: var(--white); }
  .brand--footer { left: 46px; top: 32px; font-size: 19px; color: var(--ink); }
  .brand--footer .brand__mark { width: 13px; height: 13px; background: var(--ink); }

  .metal {
    background: linear-gradient(180deg, var(--metal-light) 0%, var(--metal-mid) 45%, #e4e6e8 70%, var(--metal-dark) 100%);
  }
  .title-plate {
    position: absolute; left: 0; top: 355px; width: 699px; height: 85px;
    box-shadow: 0 2px 5px rgba(0,0,0,.4);
  }
  .title-plate__main {
    position: absolute; right: 36px; top: 8px;
    font-size: 32px; font-weight: 500; letter-spacing: .5px; color: #151515;
  }
  .title-plate__sub {
    position: absolute; right: 36px; top: 45px;
    font-size: 23px; font-weight: 500; letter-spacing: .3px; color: #151515;
  }
  .screw {
    position: absolute; width: 10px; height: 10px; border-radius: 50%;
    background: radial-gradient(circle at 35% 35%, #f5f5f5, #8a8e92 70%, #5d6166);
    box-shadow: 0 0 0 1px rgba(0,0,0,.2);
  }

  /* Back */
  .back-header {
    position: absolute; left: 0; top: 0; width: 100%; height: 107px;
    background:
      radial-gradient(ellipse 30% 60% at 55% 60%, rgba(130,210,210,.4), transparent 70%),
      radial-gradient(ellipse 25% 60% at 88% 30%, rgba(7,63,68,.5), transparent 70%),
      linear-gradient(90deg, var(--teal-deep) 0%, var(--teal) 60%, #237f85 100%);
  }
  .back-header__title {
    position: absolute; left: 36px; top: 30px;
    padding-left: 12px; border-left: 2px solid var(--white);
    font-size: 29.5px; line-height: 29px; font-weight: 500; color: var(--white);
    text-transform: uppercase; letter-spacing: .3px;
  }
  .intro {
    position: absolute; left: 32px; top: 120px; width: 685px;
    font-size: 12.1px; line-height: 15.5px; color: var(--ink);
  }
  .services {
    position: absolute; left: 32px; top: 176px;
    display: grid; grid-template-columns: 179px 179px; column-gap: 19px; row-gap: 10px;
  }
  .service { position: relative; height: 94px; }
  .service__photo { position: absolute; inset: 0; }
  .service__photo--lathe { background: linear-gradient(135deg, #5a5f62, #b8bcbe 50%, #3a3e40); }
  .service__photo--mill { background: linear-gradient(160deg, #8f9396, #d2d4d5 45%, #505457); }
  .service__photo--swiss { background: linear-gradient(135deg, #3b3f42, #8d8577 55%, #2b2e30); }
  .service__photo--axis { background: linear-gradient(135deg, #1f2224, #8a8f93 60%, #c9cccf); }
  .service__label {
    position: absolute; left: 0; bottom: 0; width: 100%; height: 16px;
    background: var(--orange); color: var(--white);
    font-size: 12px; line-height: 16px; text-align: center; text-transform: uppercase;
  }
  .capabilities {
    position: absolute; left: 446px; top: 175px; list-style: none;
    font-size: 12.4px; line-height: 16.8px; color: var(--orange-text);
  }
  .capabilities li { position: relative; padding-left: 16px; }
  .capabilities li::before {
    content: ""; position: absolute; left: 0; top: 5px;
    width: 7px; height: 7px; border-radius: 50%; background: var(--orange-text);
  }
  .contact-plate {
    position: absolute; left: 0; top: 390px; width: 100%; height: 88px;
  }
  .contact {
    position: absolute; display: flex; align-items: center; gap: 9px;
    font-size: 12.5px; font-weight: 600; color: var(--ink);
  }
  .contact svg { width: 20px; height: 20px; flex: none; }
</style>
</head>
<body>

<section class="card card--front">
  <div class="cover-photo" role="img" aria-label="Close-up photograph of machined steel gears, toned in teal"></div>
  <div class="brand brand--cover"><span class="brand__mark"></span>Ridgeline Controls</div>
  <div class="title-plate metal">
    <div class="title-plate__main">PRECISION</div>
    <div class="title-plate__sub">CNC MACHINING</div>
    <span class="screw" style="left:681px;top:11px"></span>
    <span class="screw" style="left:681px;top:65px"></span>
  </div>
</section>

<section class="card card--back">
  <div class="back-header" role="img" aria-label="Teal-toned photograph of a CNC machine spindle at work">
    <h1 class="back-header__title">Computer Numeric<br>Control (CNC)</h1>
  </div>
  <p class="intro">CNC machining offers the most efficient method of producing steel and plastic components. The CNC is programmed using computer code to generate a digital machining process that can be repeated and precisely controlled. Repetitive tasks such as drilling, threading, and tapping are made simple using this technology.</p>

  <div class="services">
    <figure class="service">
      <div class="service__photo service__photo--lathe" role="img" aria-label="Photograph of a lathe turning a metal part"></div>
      <figcaption class="service__label">Lathe / Turning</figcaption>
    </figure>
    <figure class="service">
      <div class="service__photo service__photo--mill" role="img" aria-label="Photograph of an end mill cutting a metal block"></div>
      <figcaption class="service__label">Milling</figcaption>
    </figure>
    <figure class="service">
      <div class="service__photo service__photo--swiss" role="img" aria-label="Photograph of Swiss screw machine tooling"></div>
      <figcaption class="service__label">Swiss</figcaption>
    </figure>
    <figure class="service">
      <div class="service__photo service__photo--axis" role="img" aria-label="Photograph of a 5-axis machining head shaping a part"></div>
      <figcaption class="service__label">5-Axis</figcaption>
    </figure>
  </div>

  <ul class="capabilities">
    <li>Lathe &amp; Turning Centers up to 36" Dia.</li>
    <li>Mill &amp; Machining Centers up to 120" L</li>
    <li>Complex Multi-Axis Machining up to 8-Axis</li>
    <li>Swiss Screw Machining</li>
    <li>Deep Hole Drilling/Trepanning</li>
    <li>CNC Honing &amp; Grinding</li>
    <li>CNC Laser &amp; Cladding</li>
    <li>CNC Press</li>
    <li>CNC Plasma &amp; Water Jet</li>
    <li>Oil Field and Custom Threading</li>
    <li>3D Surfacing and Mold Machining</li>
    <li>Large Capacity Band Saw Cutting</li>
  </ul>

  <footer class="contact-plate metal">
    <span class="screw" style="left:19px;top:17px"></span>
    <span class="screw" style="left:19px;top:60px"></span>
    <span class="screw" style="left:701px;top:17px"></span>
    <span class="screw" style="left:701px;top:60px"></span>
    <div class="brand brand--footer"><span class="brand__mark"></span>Ridgeline Controls</div>

    <div class="contact" style="left:364px;top:19px">
      <svg viewBox="0 0 20 20" aria-hidden="true"><rect x="5" y="1" width="10" height="18" rx="2" fill="none" stroke="#1d1d1d" stroke-width="1.6"/><line x1="8.5" y1="16" x2="11.5" y2="16" stroke="#1d1d1d" stroke-width="1.4"/></svg>
      <span>780 555 0142</span>
    </div>
    <div class="contact" style="left:364px;top:50px">
      <svg viewBox="0 0 20 20" aria-hidden="true"><rect x="2" y="7" width="16" height="11" rx="1.5" fill="#1d1d1d"/><rect x="6" y="2" width="8" height="6" fill="none" stroke="#1d1d1d" stroke-width="1.5"/><rect x="5" y="10" width="2" height="2" fill="#fff"/><rect x="9" y="10" width="2" height="2" fill="#fff"/><rect x="13" y="10" width="2" height="2" fill="#fff"/><rect x="5" y="13.5" width="2" height="2" fill="#fff"/><rect x="9" y="13.5" width="2" height="2" fill="#fff"/><rect x="13" y="13.5" width="2" height="2" fill="#fff"/></svg>
      <span>888 555 0199</span>
    </div>
    <div class="contact" style="left:494px;top:19px">
      <svg viewBox="0 0 20 20" aria-hidden="true"><rect x="1" y="4" width="18" height="12" fill="none" stroke="#1d1d1d" stroke-width="1.6"/><polyline points="1,4 10,11 19,4" fill="none" stroke="#1d1d1d" stroke-width="1.6"/></svg>
      <span>info@ridgelinecontrols.ca</span>
    </div>
    <div class="contact" style="left:494px;top:50px">
      <svg viewBox="0 0 20 20" aria-hidden="true"><circle cx="10" cy="10" r="8.5" fill="none" stroke="#1d1d1d" stroke-width="1.5"/><ellipse cx="10" cy="10" rx="3.8" ry="8.5" fill="none" stroke="#1d1d1d" stroke-width="1.2"/><line x1="1.5" y1="10" x2="18.5" y2="10" stroke="#1d1d1d" stroke-width="1.2"/><line x1="3" y1="5.5" x2="17" y2="5.5" stroke="#1d1d1d" stroke-width="1"/><line x1="3" y1="14.5" x2="17" y2="14.5" stroke="#1d1d1d" stroke-width="1"/></svg>
      <span>www.ridgelinecontrols.ca</span>
    </div>
  </footer>
</section>

</body>
</html>
```